Business Cards for Velder Works
Velder Works
Project: Business Cards for Velder Works
Business Cards for Velder Works - Financial Services
Creative Brief
Professional
Oscar T. Grell, JR.
Founder / CEO
412 Dornway Ln 300 Pelkin Court Suite 500 Pelkin PA 19588 2276 North Oak Ave Tremont MD 21977
oscar.grell@qzt-mail.com

```html
<!DOCTYPE html>
<html lang="en">
<head>
<meta charset="utf-8">
<title>Velder Works – Business Cards</title>
<link rel="stylesheet" href="https://fonts.googleapis.com/css2?family=Open+Sans:wght@400;600;700&display=swap">
<style>
  :root {
    --stage: #1c1c1e;
    --card-white: #ffffff;
    --card-grey: #f3f3f3;
    --ink: #111111;
    --text: #333333;
    --red: #d3111b;
    --black: #000000;
  }
  * { margin: 0; padding: 0; box-sizing: border-box; }
  html, body { width: 1200px; height: 740px; overflow: hidden; }
  body {
    background: var(--stage);
    font-family: "Open Sans", Arial, sans-serif;
    position: relative;
  }
  .card {
    position: absolute;
    width: 525px;
    height: 300px;
    background: var(--card-white);
    overflow: hidden;
    box-shadow: 0 4px 14px rgba(0,0,0,.55);
  }
  .card--grey { background: var(--card-grey); }
  .card--back { background: var(--black); }
  .card-a { left: 59px; top: 51px; }
  .card-b { left: 628px; top: 51px; }
  .card-c { left: 59px; top: 393px; }
  .card-d { left: 628px; top: 393px; }

  .swoosh { position: absolute; left: 0; top: 0; width: 525px; height: 300px; }

  .brand-name {
    position: absolute;
    left: 40px; top: 44px;
    font-size: 34px;
    font-weight: 700;
    letter-spacing: 1px;
    color: var(--red);
    text-transform: uppercase;
    white-space: nowrap;
  }
  .card--back .brand-name {
    left: 0; right: 0; top: 126px;
    text-align: center;
    color: #ffffff;
    font-size: 38px;
  }

  .contact {
    position: absolute;
    right: 25px; top: 140px;
    text-align: right;
    font-size: 12.5px;
    color: var(--text);
    line-height: 20px;
  }
  .contact-line { display: flex; justify-content: flex-end; align-items: center; gap: 9px; }
  .contact-line svg { width: 14px; height: 14px; fill: #222; flex: none; }
  .address { margin-top: 2px; line-height: 19px; }

  .person { position: absolute; left: 33px; top: 238px; }
  .person-name { font-size: 17px; font-weight: 700; color: var(--ink); }
  .person-title { font-size: 13.5px; color: var(--red); margin-top: 1px; }
</style>
</head>
<body>

<svg width="0" height="0" style="position:absolute">
  <defs>
    <symbol id="icon-phone" viewBox="0 0 16 16"><path d="M1 5c0-2 3-3 7-3s7 1 7 3v1h-4V5H5v1H1zM4 7h8l2 6H2zm4 1.5a2 2 0 1 0 0 4 2 2 0 0 0 0-4z"/></symbol>
    <symbol id="icon-mobile" viewBox="0 0 16 16"><path d="M4 0h8a1 1 0 0 1 1 1v14a1 1 0 0 1-1 1H4a1 1 0 0 1-1-1V1a1 1 0 0 1 1-1zm1 2v10h6V2zm3 11a1 1 0 1 0 0 2 1 1 0 0 0 0-2z"/></symbol>
    <symbol id="icon-fax" viewBox="0 0 16 16"><path d="M4 1h8v4H4zM1 6h14v6h-3v3H4v-3H1zm4 4v4h6v-4z"/></symbol>
    <symbol id="icon-mail" viewBox="0 0 16 16"><path d="M1 3h14v10H1zm1.5 1.2L8 8.6l5.5-4.4zM2 5.5V12h12V5.5L8 10z"/></symbol>
  </defs>
</svg>

<!-- Front: founder -->
<div class="card card-a">
  <svg class="swoosh" viewBox="0 0 525 300" aria-hidden="true">
    <path d="M0 0H525V8C430 85 320 168 190 176C110 180 45 162 0 138Z" fill="#000"/>
    <path d="M0 150C70 172 160 180 250 176C170 184 80 178 0 158Z" fill="#000"/>
    <path d="M220 176C340 166 450 96 525 8V22C448 104 340 170 220 176Z" fill="#d3111b"/>
  </svg>
  <div class="brand-name">Velder Works</div>
  <div class="contact">
    <div class="contact-line">555-318-4908 <svg><use href="#icon-phone"/></svg></div>
    <div class="contact-line">555-430-2291 <svg><use href="#icon-mobile"/></svg></div>
    <div class="contact-line">555-318-4929 <svg><use href="#icon-fax"/></svg></div>
    <div class="contact-line">oscar.grell@qzt-mail.com <svg><use href="#icon-mail"/></svg></div>
    <div class="address">412 Dornway Ln 300 Pelkin Court<br>Suite 500, Pelkin PA 19588<br>2276 North Oak Ave, Tremont MD 21977</div>
  </div>
  <div class="person">
    <div class="person-name">Oscar T. Grell, JR.</div>
    <div class="person-title">Founder / CEO</div>
  </div>
</div>

<!-- Front: senior strategist -->
<div class="card card--grey card-b">
  <svg class="swoosh" viewBox="0 0 525 300" aria-hidden="true">
    <path d="M0 0H525V8C430 85 320 168 190 176C110 180 45 162 0 138Z" fill="#000"/>
    <path d="M0 150C70 172 160 180 250 176C170 184 80 178 0 158Z" fill="#000"/>
    <path d="M220 176C340 166 450 96 525 8V22C448 104 340 170 220 176Z" fill="#d3111b"/>
  </svg>
  <div class="brand-name">Velder Works</div>
  <div class="contact">
    <div class="contact-line">555-749-1180 <svg><use href="#icon-phone"/></svg></div>
    <div class="contact-line">555-726-0934 <svg><use href="#icon-mobile"/></svg></div>
    <div class="contact-line">555-749-2265 <svg><use href="#icon-fax"/></svg></div>
    <div class="contact-line">oscargrellsr@pmail-box.com <svg><use href="#icon-mail"/></svg></div>
    <div class="address">412 Dornway Ln 300 Pelkin Court<br>Suite 500, Pelkin PA 19588<br>2276 North Oak Ave, Tremont MD 21977</div>
  </div>
  <div class="person">
    <div class="person-name">Oscar T. Grell Sr.</div>
    <div class="person-title">Senior Strategist</div>
  </div>
</div>

<!-- Front: advisor -->
<div class="card card--grey card-c">
  <svg class="swoosh" viewBox="0 0 525 300" aria-hidden="true">
    <path d="M0 0H525V8C430 85 320 168 190 176C110 180 45 162 0 138Z" fill="#000"/>
    <path d="M0 150C70 172 160 180 250 176C170 184 80 178 0 158Z" fill="#000"/>
    <path d="M220 176C340 166 450 96 525 8V22C448 104 340 170 220 176Z" fill="#d3111b"/>
  </svg>
  <div class="brand-name">Velder Works</div>
  <div class="contact">
    <div class="contact-line">555-318-4902 <svg><use href="#icon-phone"/></svg></div>
    <div class="contact-line">555-842-0617 <svg><use href="#icon-mobile"/></svg></div>
    <div class="contact-line">555-318-4929 <svg><use href="#icon-fax"/></svg></div>
    <div class="contact-line">dale.ferrow@qzt-mail.com <svg><use href="#icon-mail"/></svg></div>
    <div class="address">412 Dornway Ln 300 Pelkin Court<br>Suite 500, Pelkin PA 19588<br>2276 North Oak Ave, Tremont MD 21977</div>
  </div>
  <div class="person">
    <div class="person-name">Dale M. Ferrow</div>
    <div class="person-title">Private Wealth Advisor</div>
  </div>
</div>

<!-- Back -->
<div class="card card--back card-d">
  <div class="brand-name">Velder Works</div>
</div>

</body>
</html>
```